Tovek - Business Card Design

Design a modern masculine business card for our business

Target Market(s)

Private Market

Industry/Entity Type

Construction

Contact Information for Business Card

Company Name - Name of Person - Address - email address - contact number

Font styles to use
Serif
Sans Serif

Colors
0094D4
00A9DD
6FCCEA
C7EBF8
E9F6FB
00AB8E
00BBA5
67D7C9
C6EFE9
E9F9F6
F0912C
F2A743
F7CA91
FBE8D2
FDF5EE

Requirements
Must have
• Use company logo provided
Nice to have
• Company Logo

```html
<!DOCTYPE html>
<html lang="en">
<head>
<meta charset="UTF-8">
<title>Tovek Construction — Business Card</title>
<link rel="stylesheet" href="https://fonts.googleapis.com/css2?family=Orbitron:wght@700&family=Montserrat:wght@400;500&display=swap">
<style>
  :root {
    --backdrop: #7d6347;
    --card-white: #ffffff;
    --card-dark: #1d1d1d;
    --band-dark: #222222;
    --orange: #f0722c;
    --ink: #1f1f1f;
    --text: #262626;
    --silver: #8d8d8d;
  }
  * { margin: 0; padding: 0; box-sizing: border-box; }
  html, body { width: 900px; height: 1200px; overflow: hidden; }
  body {
    background: var(--backdrop);
    position: relative;
    font-family: "Montserrat", Arial, sans-serif;
  }
  .card {
    position: absolute;
    left: 80px;
    width: 742px;
    height: 440px;
    border-radius: 30px;
    overflow: hidden;
    box-shadow: 0 6px 14px rgba(0,0,0,.35);
  }
  .card--front { top: 132px; background: var(--card-white); }
  .card--back { top: 640px; background: var(--card-dark); }

  .wordmark {
    position: absolute;
    font-family: "Orbitron", Arial, sans-serif;
    font-weight: 700;
    line-height: 1;
  }
  .wordmark__name { display: block; }
  .wordmark__sub { display: block; }

  .card--front .wordmark { left: 48px; top: 192px; color: var(--ink); }
  .card--front .wordmark__name { font-size: 66px; letter-spacing: 2px; }
  .card--front .wordmark__sub { font-size: 15px; margin-top: 8px; margin-left: 4px; letter-spacing: .5px; }

  .divider {
    position: absolute;
    left: 402px; top: 133px;
    width: 2px; height: 185px;
    background: var(--orange);
  }
  .contact {
    position: absolute;
    left: 430px; top: 128px;
    color: var(--text);
    font-size: 16px;
  }
  .contact__name {
    font-family: "Orbitron", Arial, sans-serif;
    font-weight: 700;
    font-size: 22px;
    color: var(--orange);
    letter-spacing: .5px;
  }
  .contact__role { margin-top: 2px; }
  .contact__address { margin-top: 22px; line-height: 20px; }
  .contact__lines { list-style: none; margin-top: 20px; }
  .contact__lines li { display: flex; align-items: center; height: 22px; }
  .contact__lines svg { width: 13px; height: 13px; margin-right: 13px; fill: var(--orange); }

  .band { position: absolute; left: 0; bottom: 0; width: 742px; height: 32px; }

  .card--back .wordmark { left: 72px; top: 150px; color: var(--silver); }
  .card--back .wordmark__name { font-size: 138px; letter-spacing: 6px; }
  .card--back .wordmark__sub { font-size: 26px; margin-top: 12px; margin-left: 270px; letter-spacing: 1px; }
</style>
</head>
<body>
  <section class="card card--front">
    <div class="wordmark">
      <span class="wordmark__name">TOVEK</span>
      <span class="wordmark__sub">CONSTRUCTION, INC</span>
    </div>
    <div class="divider"></div>
    <div class="contact">
      <h1 class="contact__name">DANIEL HARPER</h1>
      <p class="contact__role">CEO &amp; Founder</p>
      <p class="contact__address">48 Ridgeway Lane, Suite 204<br>Hollins, PA 17520</p>
      <ul class="contact__lines">
        <li><svg viewBox="0 0 16 16"><path d="M2 6c0-2 2-3 6-3s6 1 6 3v1h-3V5.5H5V7H2z M4 8h8l2 5H2z"/></svg>555-214-0837</li>
        <li><svg viewBox="0 0 16 16"><path d="M1 4h14v1l-7 5-7-5z M1 6.5l7 5 7-5V13H1z"/></svg>info@tovekconstruction.com</li>
        <li><svg viewBox="0 0 16 16"><path d="M8 1a7 7 0 1 0 0 14A7 7 0 0 0 8 1zm-1 2c-1 1-2 2-1 3s2 0 2 2-2 1-2 3 1 2 2 3a5.5 5.5 0 0 1-1-11zm3 1c1 1 0 2 1 3s2 0 2 1a5.5 5.5 0 0 0-3-4z"/></svg>www.tovekconstruction.com</li>
      </ul>
    </div>
    <svg class="band" viewBox="0 0 742 32" aria-hidden="true">
      <rect width="742" height="32" fill="var(--band-dark)"/>
      <polygon points="0,0 200,0 218,32 0,32" fill="var(--card-white)"/>
      <g fill="var(--orange)">
        <polygon points="6,0 30,0 48,32 14,32"/>
        <polygon points="42,0 66,0 84,32 60,32"/>
        <polygon points="78,0 102,0 120,32 96,32"/>
        <polygon points="114,0 138,0 156,32 132,32"/>
        <polygon points="150,0 176,0 194,32 168,32"/>
      </g>
    </svg>
  </section>

  <section class="card card--back">
    <div class="wordmark">
      <span class="wordmark__name">TOVEK</span>
      <span class="wordmark__sub">CONSTRUCTION, INC</span>
    </div>
  </section>
</body>
</html>
```